Im looking to drive the very foundation of our business into a differnet direction. With a team of

We need to develop firstly a corporate profile that really gets the attentions of the reader. From here I want then to develop a report format (template) that we can overlay the reports we do. We have a logo and tat that can be found at www.brindlewoodgroup.com.au. I want to stay with the lime green and blue to be sure we stay on the same branding message we already have.

The final design should communicate as the business is named Corvane Ridge Tallmark Partners Australia.

Download Purchased Pixelmoor image here:
https://www.filequarry.net/s/k27vbq81ntaxzre/pixelmoor_504918263.jpg?dl=0

Target Market(s)

Large corporate clents

Industry/Entity Type

Consulting

Requirements
Must have
• Photos not animated pictures

```html
<!DOCTYPE html>
<html lang="en">
<head>
<meta charset="utf-8">
<title>Corvane Ridge – Corporate Profile and Report Template</title>
<link href="https://fonts.googleapis.com/css2?family=Arimo:wght@400;700&display=swap" rel="stylesheet">
<style>
  :root {
    --canvas: #cccccc;
    --paper: #ffffff;
    --navy: #25408f;
    --lime: #82c55a;
    --tile-hygiene: #82c55a;
    --tile-ohs: #5182b0;
    --tile-env: #f5be3e;
    --tile-lab: #a8d454;
    --tile-property: #65a0d6;
    --tile-programs: #e8db45;
    --ink: #222222;
  }
  * { margin: 0; padding: 0; box-sizing: border-box; }
  html, body { width: 1200px; height: 1000px; overflow: hidden; }
  body {
    background: var(--canvas);
    font-family: "Arimo", Arial, sans-serif;
    position: relative;
  }
  .page {
    position: absolute;
    top: 115px;
    width: 544px;
    height: 770px;
    background: var(--paper);
    box-shadow: 6px 6px 6px rgba(0,0,0,0.45);
  }
  .page--cover { left: 30px; }
  .page--report { left: 613px; }
  .page svg.rules { position: absolute; inset: 0; }

  .brand { position: absolute; display: flex; align-items: center; }
  .brand__dot { border-radius: 50%; background: var(--lime); flex: none; }
  .brand__text { display: flex; flex-direction: column; align-items: flex-end; }
  .brand__name { color: var(--navy); font-weight: 700; letter-spacing: -1px; white-space: nowrap; }
  .brand__tagline { color: var(--ink); font-weight: 400; white-space: nowrap; }

  .cover-brand { left: 88px; top: 86px; }
  .cover-brand .brand__dot { width: 48px; height: 48px; margin-right: 14px; }
  .cover-brand .brand__name { font-size: 42px; line-height: 52px; }
  .cover-brand .brand__tagline { font-size: 12.5px; line-height: 14px; }

  .report-brand { left: 30px; top: 30px; }
  .report-brand .brand__dot { width: 38px; height: 38px; margin-right: 9px; }
  .report-brand .brand__name { font-size: 32px; line-height: 40px; }
  .report-brand .brand__tagline { font-size: 9.5px; line-height: 11px; }

  .services {
    position: absolute;
    left: 64px;
    top: 256px;
    display: grid;
    grid-template-columns: repeat(3, 127px);
    grid-template-rows: repeat(2, 133px);
    column-gap: 18px;
    row-gap: 19px;
    list-style: none;
  }
  .service {
    padding: 9px 12px;
    color: #fff;
    font-weight: 700;
    font-size: 12px;
    line-height: 15px;
  }
  .service--hygiene { background: var(--tile-hygiene); }
  .service--ohs { background: var(--tile-ohs); }
  .service--env { background: var(--tile-env); }
  .service--lab { background: var(--tile-lab); }
  .service--property { background: var(--tile-property); }
  .service--programs { background: var(--tile-programs); }

  .footer-mark {
    position: absolute;
    left: 247px;
    top: 683px;
    width: 50px;
    display: flex;
    flex-direction: column;
    align-items: center;
  }
  .footer-mark__dot { width: 30px; height: 30px; border-radius: 50%; background: var(--lime); }
  .footer-mark__name { margin-top: 4px; color: var(--navy); font-weight: 700; font-size: 14px; line-height: 15px; }
</style>
</head>
<body>

  <section class="page page--cover" aria-label="Corporate profile cover">
    <svg class="rules" width="544" height="770" aria-hidden="true">
      <line x1="32" y1="234.5" x2="512" y2="234.5" stroke="var(--navy)" stroke-width="2"/>
      <line x1="32" y1="562" x2="512" y2="562" stroke="var(--navy)" stroke-width="2"/>
      <line x1="50" y1="720" x2="247" y2="720" stroke="var(--lime)" stroke-width="2"/>
      <line x1="32" y1="730" x2="247" y2="730" stroke="var(--lime)" stroke-width="2"/>
      <line x1="297" y1="720" x2="494" y2="720" stroke="var(--lime)" stroke-width="2"/>
      <line x1="297" y1="730" x2="512" y2="730" stroke="var(--lime)" stroke-width="2"/>
    </svg>

    <div class="brand cover-brand">
      <span class="brand__dot"></span>
      <div class="brand__text">
        <span class="brand__name">Corvane Ridge</span>
        <span class="brand__tagline">HEALTH SAFETY ENVIRONMENT</span>
      </div>
    </div>

    <ul class="services">
      <li class="service service--hygiene">Occupational<br>Hygiene</li>
      <li class="service service--ohs">Occupational<br>Health and Safety</li>
      <li class="service service--env">Environmental<br>Solutions</li>
      <li class="service service--lab">Laboratory</li>
      <li class="service service--property">Property<br>Services</li>
      <li class="service service--programs">SteadyPace<br>Programs</li>
    </ul>

    <div class="footer-mark">
      <span class="footer-mark__dot"></span>
      <span class="footer-mark__name">CRT</span>
    </div>
  </section>

  <section class="page page--report" aria-label="Report template page">
    <svg class="rules" width="544" height="770" aria-hidden="true">
      <line x1="37" y1="89" x2="310" y2="89" stroke="var(--lime)" stroke-width="1.5"/>
      <line x1="418" y1="78" x2="506" y2="78" stroke="var(--lime)" stroke-width="1.5"/>
      <line x1="392" y1="84" x2="506" y2="84" stroke="var(--lime)" stroke-width="1.5"/>
      <line x1="372" y1="89" x2="506" y2="89" stroke="var(--lime)" stroke-width="1.5"/>
      <line x1="32" y1="95" x2="512" y2="95" stroke="var(--navy)" stroke-width="2"/>
      <line x1="50" y1="720" x2="247" y2="720" stroke="var(--lime)" stroke-width="2"/>
      <line x1="32" y1="730" x2="247" y2="730" stroke="var(--lime)" stroke-width="2"/>
      <line x1="297" y1="720" x2="494" y2="720" stroke="var(--lime)" stroke-width="2"/>
      <line x1="297" y1="730" x2="512" y2="730" stroke="var(--lime)" stroke-width="2"/>
    </svg>

    <div class="brand report-brand">
      <span class="brand__dot"></span>
      <div class="brand__text">
        <span class="brand__name">Corvane Ridge</span>
        <span class="brand__tagline">HEALTH SAFETY ENVIRONMENT</span>
      </div>
    </div>

    <div class="footer-mark">
      <span class="footer-mark__dot"></span>
      <span class="footer-mark__name">CRT</span>
    </div>
  </section>

</body>
</html>
```